Smile club flyer design

I am launching an office smile club and would like a design that sits my branding and that is appealing to customers. I have a design (I need a new one) that has all the information.
My website is maplecrestdentalcarewv.com
Brand color is green. The design can be any color

Target Market(s)

Ages 30+

Industry/Entity Type

Dental

Font styles to use
Serif

Requirements
Must have
• Appealing to patients

```html
<!DOCTYPE html>
<html lang="en">
<head>
<meta charset="utf-8">
<title>Maplecrest Dental Care – Smile Club Membership</title>
<link rel="stylesheet" href="https://fonts.googleapis.com/css2?family=Poppins:wght@500;600;700;800&family=Roboto+Condensed:wght@500;600&family=Libre+Baskerville:wght@400;700&family=Kaushan+Script&family=Cormorant+Garamond:wght@700&display=swap">
<style>
:root{
  --backdrop:#3a3a3a;
  --green:#17b34f;
  --green-deep:#0a9a43;
  --lime:#8dc63f;
  --olive:#4a6323;
  --forest:#0a4a20;
  --pill:#374b17;
  --ink:#0d3a1c;
  --text:#2f3b2c;
  --orange:#f0941e;
  --mint:#8fe8b5;
  --white:#ffffff;
  --cream:#eef8e3;
}
*{margin:0;padding:0;box-sizing:border-box}
html,body{width:1011px;height:1200px;overflow:hidden;background:var(--backdrop)}
.flyer{position:absolute;left:173px;top:101px;width:665px;height:998px;overflow:hidden;
  background:linear-gradient(180deg,var(--green-deep) 0%,var(--green) 30%,#27bf5c 55%,#1fae4d 100%);
  font-family:"Poppins",sans-serif;color:var(--white)}
.portrait{position:absolute;left:446px;top:0;width:219px;height:266px;
  background:radial-gradient(ellipse at 55% 30%,#c98b6a 0%,#8f4a2b 30%,#1f9e52 62%,#12a34a 100%)}
.brand{position:absolute;left:222px;top:18px;width:240px;text-align:center}
.brand-name{font-family:"Libre Baskerville",serif;font-size:33px;line-height:1}
.brand-sub{font-size:10px;letter-spacing:4px;font-weight:600;margin-top:4px}
.intro{position:absolute;left:180px;top:110px;width:300px;text-align:center;
  font-family:"Kaushan Script",cursive;font-size:44px}
.title{position:absolute;left:0;width:665px;text-align:center;font-weight:700;line-height:1}
.title-main{top:172px;font-size:100px;letter-spacing:-2px;left:50px;width:565px}
.title-sub{top:265px;font-size:49px;letter-spacing:-1px}
.tagline{position:absolute;left:49px;top:325px;width:557px;height:37px;border-radius:19px;
  background:var(--pill);text-align:center;font-size:14px;font-weight:600;line-height:37px}
.plan{position:absolute;top:387px;width:168px;height:304px}
.plan-body{position:absolute;inset:0;background:var(--white);border-radius:0 0 84px 84px/0 0 110px 110px}
.plan-head{position:absolute;top:14px;left:0;width:100%;text-align:center;line-height:1.05}
.plan-name{font-size:22px;font-weight:800}
.plan-kind{font-size:15px;font-weight:500}
.plan-price{position:absolute;top:64px;left:-11px;width:190px;height:65px;text-align:center;border-radius:3px}
.plan-price b{display:block;font-size:38px;font-weight:800;line-height:1.2;padding-top:2px}
.plan-price span{display:block;font-size:12px;margin-top:-4px}
.features{position:absolute;top:156px;left:13px;right:8px;list-style:none;
  font-family:"Roboto Condensed",sans-serif;font-weight:500;font-size:10px;color:var(--text);line-height:1.3}
.features li{position:relative;padding-left:13px;margin-bottom:9px}
.features svg{position:absolute;left:0;top:2px;width:9px;height:9px}
.core{left:41px}.core .plan-name{color:var(--lime);font-size:23px}.core .plan-kind{color:var(--lime)}
.core .plan-price{background:var(--lime)}
.bright{left:254px}.bright .plan-name,.bright .plan-kind{color:var(--olive)}
.bright .plan-price{background:var(--olive)}
.total{left:471px}.total .plan-head{top:8px}.total .plan-name,.total .plan-kind{color:var(--green)}
.total .plan-price{background:var(--forest)}
.join{position:absolute;left:34px;top:700px;width:597px;height:247px;border-radius:40px 0 0 0;background:var(--cream)}
.join-title{position:absolute;left:30px;top:34px;font-family:"Cormorant Garamond",serif;font-weight:700;font-size:34px;color:var(--orange)}
.join-phone{position:absolute;left:34px;top:70px;font-size:38px;font-weight:800;color:var(--ink);letter-spacing:-0.5px}
.join-finance{position:absolute;left:30px;top:132px;font-size:16.5px;font-weight:600;color:var(--ink)}
.partners{position:absolute;left:28px;top:182px;display:flex;gap:40px;font-size:19px;font-weight:600;color:#3b4658}
.partners span{display:flex;align-items:center;gap:6px}
.partners i{display:inline-block;width:12px;height:12px;border-radius:50%;background:#3b4658}
.refresh{position:absolute;left:411px;top:700px;width:219px;height:247px;background:#053616;border-radius:0 0 60px 0}
.refresh-ring{position:absolute;left:29px;top:14px;width:162px;height:210px;border:2px solid var(--mint);border-radius:50%}
.refresh-new{position:absolute;left:73px;top:5px;width:70px;height:33px;background:var(--orange);border-radius:14px 14px 0 0;
  font-family:"Cormorant Garamond",serif;font-weight:700;font-size:20px;text-align:center;line-height:33px}
.refresh-text{position:absolute;left:0;width:100%;text-align:center;line-height:1}
.r-smile{top:46px;font-size:36px;font-weight:800}
.r-label{top:82px;font-size:11px;font-weight:500}
.r-price{top:96px;font-size:35px;font-weight:800;color:#8ee04a}
.r-items{top:138px;font-family:"Roboto Condensed",sans-serif;font-weight:600;font-size:13.5px;line-height:22px}
.r-offer{top:221px;font-family:"Kaushan Script",cursive;font-size:18px;color:var(--orange)}
.fee{position:absolute;left:0;top:958px;width:665px;text-align:center;font-size:13px;font-weight:600}
</style>
</head>
<body>
<main class="flyer">
  <div class="portrait" role="img" aria-label="Photo of a smiling woman in a green sweater pointing to her smile"></div>

  <header class="brand">
    <div class="brand-name">Maplecrest</div>
    <div class="brand-sub">— DENTAL CARE —</div>
  </header>

  <div class="intro">Introducing</div>
  <h1 class="title title-main">SMILE CLUB</h1>
  <h2 class="title title-sub">MEMBERSHIP</h2>
  <div class="tagline">AFFORDABLE DENTAL CARE&nbsp; - NO INSURANCE REQUIRED</div>

  <svg width="0" height="0" style="position:absolute">
    <symbol id="tick" viewBox="0 0 10 10"><circle cx="5" cy="5" r="5" fill="currentColor"/><path d="M2.7 5.2l1.6 1.6 3-3.2" stroke="#fff" stroke-width="1.4" fill="none"/></symbol>
  </svg>

  <section class="plan core">
    <div class="plan-body"></div>
    <div class="plan-head"><div class="plan-name">CORE CARE</div><div class="plan-kind">PREVENTIVE</div></div>
    <div class="plan-price"><b>$39</b><span>/MONTH</span></div>
    <ul class="features" style="color:var(--text)">
      <li><svg style="color:#8dc63f"><use href="#tick"/></svg>Comprehensive Annual Exam</li>
      <li><svg style="color:#8dc63f"><use href="#tick"/></svg>2 Professional Cleanings per Year</li>
      <li><svg style="color:#8dc63f"><use href="#tick"/></svg>Routine Bitewing X-rays</li>
      <li><svg style="color:#8dc63f"><use href="#tick"/></svg>10% Savings on Treatment</li>
    </ul>
  </section>

  <section class="plan bright">
    <div class="plan-body"></div>
    <div class="plan-head"><div class="plan-name">BRIGHT</div><div class="plan-kind">COSMETIC</div></div>
    <div class="plan-price"><b>$59</b><span>/MONTH</span></div>
    <ul class="features" style="top:165px">
      <li><svg style="color:#4a6323"><use href="#tick"/></svg>Annual In-Office Whitening (Top &amp; Bottom)</li>
      <li><svg style="color:#4a6323"><use href="#tick"/></svg>Custom Whitening Trays</li>
      <li><svg style="color:#4a6323"><use href="#tick"/></svg>15% Savings on Elective Treatment</li>
    </ul>
  </section>

  <section class="plan total">
    <div class="plan-body"></div>
    <div class="plan-head"><div class="plan-name">TOTAL SMILE</div><div class="plan-kind">PERIODONTAL</div></div>
    <div class="plan-price"><b>$89</b><span>/MONTH</span></div>
    <ul class="features" style="top:150px">
      <li><svg style="color:#17b34f"><use href="#tick"/></svg>3-4 Perio Maintenance Visits per Year</li>
      <li><svg style="color:#17b34f"><use href="#tick"/></svg>1 Comprehensive Exam</li>
      <li><svg style="color:#17b34f"><use href="#tick"/></svg>Diagnostic X-rays</li>
      <li><svg style="color:#17b34f"><use href="#tick"/></svg>15% Savings on Restorative &amp; Elective Care</li>
    </ul>
  </section>

  <section class="join">
    <div class="join-title">Join Smile Club Today!</div>
    <div class="join-phone">555-210-4830</div>
    <div class="join-finance">FLEXIBLE FINANCING&nbsp; FOR TREATMENT</div>
    <div class="partners"><span><i></i>FlexPay Health</span><span><i></i>Plumline</span></div>
  </section>

  <aside class="refresh">
    <div class="refresh-ring"></div>
    <div class="refresh-new">New</div>
    <div class="refresh-text r-smile">SMILE</div>
    <div class="refresh-text r-label">REFRESH PACKAGE</div>
    <div class="refresh-text r-price">$499</div>
    <div class="refresh-text r-items">Cleaning<br>Comprehensive Exam<br>Whitening</div>
    <div class="refresh-text r-offer">Limited Time Offer</div>
  </aside>

  <p class="fee">*$49 Lifetime Activation Fee (Non-Refundable)</p>
</main>
</body>
</html>
```